Gilded By Meadow
An Exquisite Handcrafted Jeweler
Gilded By Meadow - Jewelry
Creative Brief
Use specific fonts
use font in logo and other fonts if necessary
Modern
Lena Marsh
I do not want an address printed on my business card
Info@GildedByMeadow.com
www.GildedByMeadow.com
1. Logo on front with Tag only 2. No email to be printed on the business card
A Contemporary Beaded Couture Jeweler specializing in designing custom innovative pieces of arts that's meant to adorn your personality and enhance your natural beauty. Lena Marsh 555.304.2817 www.GildedByMeadow.com

```html
<!DOCTYPE html>
<html lang="en">
<head>
<meta charset="utf-8">
<title>Gilded By Meadow — Stationery</title>
<link href="https://fonts.googleapis.com/css2?family=Cinzel:wght@400;600&display=swap" rel="stylesheet">
<style>
  :root {
    --ink: #111111;
    --plum: #a47ba8;
    --lavender: #d9c6dd;
    --paper: #ffffff;
    --backdrop: #e6e6e8;
    --muted: #8a8a8a;
  }
  * { margin: 0; padding: 0; box-sizing: border-box; }
  html, body { width: 1200px; height: 847px; overflow: hidden; }
  body {
    position: relative;
    background: var(--backdrop);
    font-family: "Cinzel", serif;
  }
  .piece { position: absolute; background: var(--paper); }

  .brand {
    display: flex; flex-direction: column; align-items: center; justify-content: flex-end;
    background: var(--ink); color: var(--paper); text-align: center;
  }
  .brand-dot { width: 14px; height: 14px; border-radius: 50%; background: var(--plum); margin-bottom: 8px; }
  .brand-name { font-weight: 600; letter-spacing: 0.04em; line-height: 1.05; color: var(--paper); }

  /* Letterhead */
  .letterhead { left: 312px; top: 108px; width: 336px; height: 624px; overflow: hidden; }
  .letterhead .brand { position: absolute; left: 0; top: 0; width: 115px; height: 168px; padding-bottom: 18px; }
  .letterhead .brand-name { font-size: 12px; }
  .letterhead .side-band { position: absolute; left: 0; top: 168px; width: 115px; bottom: 0; background: var(--plum); }
  .letterhead .footer {
    position: absolute; left: 124px; right: 10px; bottom: 10px;
    display: flex; justify-content: flex-start; gap: 10px;
    white-space: nowrap;
    font-size: 4.3px; letter-spacing: 0; color: var(--muted);
  }

  /* Business card front */
  .card-front {
    left: 612px; top: 91px; width: 188px; height: 101px; border-radius: 8px;
    background: var(--ink); color: var(--paper);
    display: flex; flex-direction: column; align-items: center; justify-content: center;
  }
  .card-front .brand-dot { width: 12px; height: 12px; margin-bottom: 6px; }
  .card-front .brand-name { font-size: 12px; }
  .card-front .tagline { margin-top: 8px; font-size: 5.5px; letter-spacing: 0.14em; text-transform: uppercase; color: var(--lavender); }

  /* Business card back */
  .card-back {
    left: 818px; top: 196px; width: 200px; height: 108px; border-radius: 8px;
    background: var(--ink); color: var(--paper); padding: 12px 16px;
  }
  .card-back .name { text-align: center; font-size: 12px; letter-spacing: 0.06em; }
  .card-back .role { text-align: center; font-size: 6px; letter-spacing: 0.14em; text-transform: uppercase; color: var(--lavender); margin-top: 2px; }
  .card-back .about { margin-top: 8px; font-family: Georgia, serif; font-size: 4.6px; line-height: 1.5; text-align: center; color: #d8d8d8; }
  .card-back .contact { margin-top: 6px; text-align: center; font-size: 5px; letter-spacing: 0.12em; color: var(--paper); }
  .card-back .corner { position: absolute; right: -5px; top: 44px; width: 14px; height: 14px; border-radius: 50%; background: var(--plum); }

  /* Envelope back (open) */
  .envelope-back { left: 696px; top: 360px; width: 432px; height: 360px; box-shadow: 0 0 0 1px #d4d4d6; }
  .envelope-back .liner { position: absolute; left: 0; top: 0; width: 100%; height: 170px; }

  /* Envelope front */
  .envelope-front { left: 470px; top: 288px; width: 423px; height: 420px; background: none; }
  .envelope-front svg.shape { position: absolute; inset: 0; }
  .envelope-front .brand { position: absolute; left: 0; top: 60px; width: 86px; height: 120px; padding-bottom: 14px; background: none; }
  .envelope-front .brand-dot { width: 10px; height: 10px; margin-bottom: 6px; }
  .envelope-front .brand-name { font-size: 9px; }
  .envelope-front .return-line { position: absolute; left: 110px; top: 45px; font-size: 5px; letter-spacing: 0.14em; color: var(--muted); }
</style>
</head>
<body>

  <section class="piece letterhead" aria-label="Letterhead">
    <div class="brand">
      <span class="brand-dot"></span>
      <span class="brand-name">Gilded<br>By Meadow</span>
    </div>
    <div class="side-band"></div>
    <div class="footer">
      <span>555.304.2817</span>
      <span>Info@GildedByMeadow.com</span>
      <span>www.GildedByMeadow.com</span>
    </div>
  </section>

  <section class="piece card-front" aria-label="Business card front">
    <span class="brand-dot"></span>
    <span class="brand-name">Gilded By Meadow</span>
    <span class="tagline">An Exquisite Handcrafted Jeweler</span>
  </section>

  <section class="piece card-back" aria-label="Business card back">
    <p class="name">Lena Marsh</p>
    <p class="role">Lead Designer</p>
    <p class="about">A Contemporary Beaded Couture Jeweler specializing in designing custom innovative pieces of art meant to adorn your personality and enhance your natural beauty.</p>
    <p class="contact">555.304.2817 &nbsp; www.GildedByMeadow.com</p>
    <span class="corner"></span>
  </section>

  <section class="piece envelope-back" aria-label="Envelope back">
    <svg class="liner" viewBox="0 0 432 170" preserveAspectRatio="none" role="img" aria-label="Envelope flap with lavender ornamental pattern">
      <defs>
        <linearGradient id="linerTone" x1="0" y1="0" x2="0" y2="1">
          <stop offset="0" stop-color="#efe6f0"/>
          <stop offset="1" stop-color="#e3d4e6"/>
        </linearGradient>
      </defs>
      <polygon points="0,0 432,0 432,40 216,170 0,40" fill="url(#linerTone)" stroke="#d4d4d6" stroke-width="1"/>
    </svg>
  </section>

  <section class="piece envelope-front" aria-label="Envelope front">
    <svg class="shape" width="423" height="420" viewBox="0 0 423 420">
      <polygon points="0,60 86,0 423,0 423,420 0,420" fill="var(--paper)" stroke="#d4d4d6" stroke-width="1"/>
      <polygon points="0,60 86,0 86,180 0,180" fill="var(--ink)"/>
      <rect x="0" y="180" width="86" height="240" fill="var(--plum)"/>
    </svg>
    <div class="brand">
      <span class="brand-dot"></span>
      <span class="brand-name">Gilded<br>By Meadow</span>
    </div>
    <p class="return-line">www.GildedByMeadow.com</p>
  </section>

</body>
</html>
```